School Poster

Design so that these can be placed in classrooms across the school.

Attached is another design we have had done. Use a similar theme.

Consider using themes from https://calderwoodhs.lumorin.edu/

please edit Binder1 doc.

Target Market(s)

Students and teachers

```html
<!DOCTYPE html>
<html lang="en">
<head>
<meta charset="utf-8">
<title>Using AI and Other Tools Responsibly – Calderwood High</title>
<link rel="stylesheet" href="https://fonts.googleapis.com/css2?family=Montserrat:wght@800&family=Poppins:wght@300;600;700&display=swap">
<style>
  :root {
    --navy: #2f4b96;
    --navy-deep: #28418a;
    --yellow: #f2e14a;
    --yellow-soft: #f4e97c;
    --white: #ffffff;
    --ink: #3a3a3a;
    --red: #d02a2a;
    --rule: #c9c9c9;
  }
  * { margin: 0; padding: 0; box-sizing: border-box; }
  html, body { width: 849px; height: 1200px; overflow: hidden; }
  body {
    position: relative;
    background: radial-gradient(circle at 20% 10%, #3553a0 0%, var(--navy) 45%, var(--navy-deep) 100%);
    font-family: "Poppins", sans-serif;
    color: var(--ink);
  }
  .poster-title {
    position: absolute; left: 40px; top: 36px;
    font-family: "Montserrat", sans-serif; font-weight: 800;
    font-size: 54px; line-height: 62px; letter-spacing: -1.5px;
    color: var(--white); white-space: nowrap;
  }
  .school-name {
    position: absolute; left: 700px; top: 66px; width: 120px;
    text-align: center; color: var(--white);
    font-family: "Poppins", sans-serif; font-weight: 700;
    font-size: 17px; line-height: 22px;
  }
  .school-name .dot {
    display: block; width: 16px; height: 16px; border-radius: 50%;
    background: var(--yellow); margin: 0 auto 8px;
  }
  .accent-band {
    position: absolute; left: 0; top: 180px; width: 849px; height: 19px;
    background: var(--yellow);
  }
  .content-card {
    position: absolute; left: 17px; top: 234px; width: 815px; height: 903px;
    background: var(--white); border-radius: 15px;
  }
  .section-heading {
    position: absolute; left: 0; width: 849px; text-align: center;
    font-family: "Montserrat", sans-serif; font-weight: 800;
    font-size: 32px; letter-spacing: -0.5px; color: var(--navy);
    line-height: 40px;
  }
  .must-heading { top: 245px; }
  .checklist {
    position: absolute; list-style: none;
    font-weight: 600; font-size: 20px; line-height: 24.5px; color: var(--ink);
  }
  .checklist li { position: relative; padding-left: 26px; margin-bottom: 8px; }
  .checklist li svg { position: absolute; left: 0; top: 7px; }
  .checklist-left { left: 57px; top: 301px; width: 330px; }
  .checklist-right { left: 391px; top: 301px; width: 220px; }
  .illustration-ai {
    position: absolute; left: 622px; top: 278px; width: 186px; height: 192px;
    border-radius: 18px;
    background: linear-gradient(135deg, #dfe5f3 0%, #f7f0b8 100%);
  }
  .help-panel {
    position: absolute; left: 43px; top: 479px; width: 762px; height: 352px;
    background: var(--yellow-soft); border-radius: 14px;
  }
  .help-heading { top: 493px; }
  .help-note {
    position: absolute; left: 0; top: 532px; width: 849px; text-align: center;
    font-weight: 300; font-size: 22px; color: var(--navy);
  }
  .column-row { position: absolute; left: 43px; width: 762px; display: flex; }
  .column {
    width: 191px; text-align: center; position: relative;
    font-weight: 700; font-size: 20px; line-height: 23px; color: var(--ink);
  }
  .column + .column { border-left: 1px solid var(--ink); }
  .help-row { top: 596px; height: 214px; }
  .help-row .column + .column { border-left-color: #8a8550; }
  .tool-illustration {
    display: block; width: 112px; height: 112px; margin: -12px auto 16px;
    border-radius: 16px;
    background: linear-gradient(135deg, var(--navy) 0%, #5a72b4 100%);
    opacity: 0.85;
  }
  .cannot-heading { top: 850px; }
  .cannot-row { top: 899px; height: 215px; }
  .cannot-row .column + .column { border-left: 2px solid var(--rule); }
  .cannot-row .cross { display: block; margin: 0 auto 22px; }
  .footer-line {
    position: absolute; left: 0; top: 1154px; width: 849px; text-align: center;
    color: var(--white); font-weight: 700; font-size: 19px;
  }
</style>
</head>
<body>
  <h1 class="poster-title">USING AI AND OTHER<br>TOOLS RESPONSIBLY</h1>
  <div class="school-name"><span class="dot"></span>Calderwood<br>High</div>
  <div class="accent-band"></div>

  <div class="content-card"></div>

  <h2 class="section-heading must-heading">WHAT YOU MUST DO:</h2>
  <ul class="checklist checklist-left">
    <li><svg width="13" height="13" viewBox="0 0 13 13"><rect x="0.75" y="0.75" width="11.5" height="11.5" fill="none" stroke="#2f4b96" stroke-width="1.5"/><path d="M3 6.5 L5.5 9 L10 3.5" fill="none" stroke="#2f4b96" stroke-width="1.6"/></svg>Complete your own work</li>
    <li><svg width="13" height="13" viewBox="0 0 13 13"><rect x="0.75" y="0.75" width="11.5" height="11.5" fill="none" stroke="#2f4b96" stroke-width="1.5"/><path d="M3 6.5 L5.5 9 L10 3.5" fill="none" stroke="#2f4b96" stroke-width="1.6"/></svg>Demonstrate your progress (drafts, notes, planning, revisions)</li>
    <li><svg width="13" height="13" viewBox="0 0 13 13"><rect x="0.75" y="0.75" width="11.5" height="11.5" fill="none" stroke="#2f4b96" stroke-width="1.5"/><path d="M3 6.5 L5.5 9 L10 3.5" fill="none" stroke="#2f4b96" stroke-width="1.6"/></svg>Use feedback to improve your work</li>
  </ul>
  <ul class="checklist checklist-right">
    <li><svg width="13" height="13" viewBox="0 0 13 13"><rect x="0.75" y="0.75" width="11.5" height="11.5" fill="none" stroke="#2f4b96" stroke-width="1.5"/><path d="M3 6.5 L5.5 9 L10 3.5" fill="none" stroke="#2f4b96" stroke-width="1.6"/></svg>Demonstrate your understanding of the ideas in your submission</li>
  </ul>
  <div class="illustration-ai" role="img" aria-label="Line illustration of a brain joined to an AI circuit chip"></div>

  <div class="help-panel"></div>
  <h2 class="section-heading help-heading">WHAT AI CAN HELP YOU DO</h2>
  <p class="help-note">(when approved by your teacher)</p>
  <div class="column-row help-row">
    <div class="column"><span class="tool-illustration" role="img" aria-label="Brain icon with sparks"></span>Brainstorm<br>ideas</div>
    <div class="column"><span class="tool-illustration" role="img" aria-label="Checklist with magnifying glass icon"></span>Check spelling,<br>grammar and<br>clarity</div>
    <div class="column"><span class="tool-illustration" role="img" aria-label="Speaking head and phone with sound wave icon"></span>Read your work<br>aloud using<br>text-to-speech<br>tools</div>
    <div class="column"><span class="tool-illustration" role="img" aria-label="Rising bar chart with arrow and gear icon"></span>Help identify<br>areas for<br>improvement<br>in a draft</div>
  </div>

  <h2 class="section-heading cannot-heading">WHAT YOU CANNOT DO:</h2>
  <div class="column-row cannot-row">
    <div class="column"><svg class="cross" width="64" height="64" viewBox="0 0 64 64"><circle cx="32" cy="32" r="27" fill="none" stroke="#d02a2a" stroke-width="6"/><path d="M22 20 L42 44 M42 20 L22 44" stroke="#d02a2a" stroke-width="5" stroke-linecap="round"/></svg>Submit AI-<br>generated work<br>as your own</div>
    <div class="column"><svg class="cross" width="64" height="64" viewBox="0 0 64 64"><circle cx="32" cy="32" r="27" fill="none" stroke="#d02a2a" stroke-width="6"/><path d="M22 20 L42 44 M42 20 L22 44" stroke="#d02a2a" stroke-width="5" stroke-linecap="round"/></svg>Copy and paste<br>AI responses<br>without<br>acknowledging<br>or adapting<br>them</div>
    <div class="column"><svg class="cross" width="64" height="64" viewBox="0 0 64 64"><circle cx="32" cy="32" r="27" fill="none" stroke="#d02a2a" stroke-width="6"/><path d="M22 20 L42 44 M42 20 L22 44" stroke="#d02a2a" stroke-width="5" stroke-linecap="round"/></svg>Use AI tools to<br>complete the<br>whole task for<br>you</div>
    <div class="column"><svg class="cross" width="64" height="64" viewBox="0 0 64 64"><circle cx="32" cy="32" r="27" fill="none" stroke="#d02a2a" stroke-width="6"/><path d="M22 20 L42 44 M42 20 L22 44" stroke="#d02a2a" stroke-width="5" stroke-linecap="round"/></svg>Submit work<br>that does not<br>demonstrate<br>your<br>understanding</div>
  </div>

  <p class="footer-line">If you didn't create, develop and understand it, it isn't your work.</p>
</body>
</html>
```